Halvorn Crest Real estate in need of Logo design

I just started a new real estate brokerage company and need a professional, new logo design that I can incorporate through all forms of marketing and branding. I would like the business card to use both Matte finish and high gloss.

```html
<!DOCTYPE html>
<html lang="en">
<head>
<meta charset="utf-8">
<title>Halvorn Crest Real Estate – Business Card</title>
<link href="https://fonts.googleapis.com/css2?family=Oswald:wght@500&family=Work+Sans:wght@400;500&display=swap" rel="stylesheet">
<style>
  :root {
    --backdrop: #1c1c1c;
    --card: #1f1f1f;
    --card-sheen: #2b2b2b;
    --gold: #d9a232;
    --white: #f4f4f4;
  }
  * { box-sizing: border-box; margin: 0; padding: 0; }
  html, body {
    width: 1200px; height: 900px; overflow: hidden;
    background: var(--backdrop);
  }
  .canvas {
    position: relative; width: 1200px; height: 900px;
    display: flex; flex-direction: column; align-items: center; justify-content: center; gap: 40px;
  }
  .card {
    position: relative; width: 700px; height: 400px;
    background: linear-gradient(120deg, var(--card) 0%, var(--card) 55%, var(--card-sheen) 100%);
    font-family: "Work Sans", sans-serif; color: var(--white);
  }
  /* Front */
  .card-front { display: flex; flex-direction: column; align-items: center; justify-content: center; }
  .brand { display: flex; align-items: center; gap: 14px; margin-top: 10px; }
  .brand-square { width: 22px; height: 22px; background: var(--gold); }
  .brand-name {
    font-weight: 500; font-size: 30px; letter-spacing: 3px; text-transform: uppercase; color: var(--gold);
  }
  .front-url { margin-top: 70px; font-size: 17px; letter-spacing: 0.5px; }
  .front-url .url-core { color: var(--gold); }
  /* Back */
  .holder {
    position: absolute; left: 120px; top: 128px; text-align: right; width: 290px;
  }
  .holder-name {
    font-family: "Oswald", sans-serif; font-weight: 500; font-size: 38px;
    letter-spacing: 1.5px; color: var(--gold); text-transform: uppercase; line-height: 1.1;
  }
  .holder-title { font-size: 18px; margin-top: 2px; }
  .divider { position: absolute; left: 432px; top: 140px; width: 2px; height: 74px; background: var(--gold); }
  .contact-list { position: absolute; left: 455px; top: 138px; list-style: none; }
  .contact-item { display: flex; align-items: center; gap: 10px; font-size: 19px; line-height: 26px; }
  .contact-item svg { width: 13px; height: 13px; flex: none; }
  .contact-item.web { font-weight: 500; }
  .address {
    position: absolute; left: 0; right: 0; bottom: 62px; text-align: center; font-size: 20px; letter-spacing: 0.5px;
  }
</style>
</head>
<body>
<main class="canvas">
  <section class="card card-front">
    <div class="brand">
      <span class="brand-square"></span>
      <span class="brand-name">Halvorn Crest Real Estate</span>
    </div>
    <p class="front-url">www.<span class="url-core">halvorncrest</span>.com</p>
  </section>

  <section class="card card-back">
    <div class="holder">
      <h1 class="holder-name">Daniel Whitcombe</h1>
      <p class="holder-title">Director</p>
    </div>
    <span class="divider"></span>
    <ul class="contact-list">
      <li class="contact-item">
        <svg viewBox="0 0 16 16"><path d="M4 1l2.5 3.5-1.5 1.5c1 2 3 4 5 5l1.5-1.5L15 12l-2 3C7 14 2 9 1 3z" fill="var(--gold)"/></svg>
        (514) 555-0142
      </li>
      <li class="contact-item">
        <svg viewBox="0 0 16 16"><rect x="1" y="3" width="14" height="10" fill="none" stroke="var(--gold)" stroke-width="1.5"/><path d="M1 3l7 6 7-6" fill="none" stroke="var(--gold)" stroke-width="1.5"/></svg>
        info@halvorncrest.com
      </li>
      <li class="contact-item web">
        <svg viewBox="0 0 16 16" fill="none" stroke="var(--gold)" stroke-width="1.3"><circle cx="8" cy="8" r="6.5"/><ellipse cx="8" cy="8" rx="3" ry="6.5"/><path d="M1.5 8h13M2.5 4.5h11M2.5 11.5h11"/></svg>
        www.halvorncrest.com
      </li>
    </ul>
    <p class="address">218b Marlow Street, Christchurch, NZ, 8013</p>
  </section>
</main>
</body>
</html>
```